MEDICAL CLINIC LETTERHEAD

Design is a letterhead for a non-profit medical center. The name of the clinic is VITORRANE Community Health Center. Although the full name must be included, the community health center part is more of a description and should be less visible - i attached an example of what I mean by that (ATTACHED IMAGE IS AN EXAMPLE OF FONT SIZES NOT A DESIGN IDEA). Please design something modern, cool looking and unique because I can always download free templates.
Phone, email, website and etc will be added later.

Industry/Entity Type

MEDICAL

```html
<!DOCTYPE html>
<html lang="en">
<head>
<meta charset="utf-8">
<title>VITORRANE Community Health Center – Letterhead</title>
<link rel="stylesheet" href="https://fonts.googleapis.com/css2?family=Didact+Gothic&family=Roboto:wght@400;700&display=swap">
<style>
  :root {
    --backdrop: #e7e7e7;
    --paper-light: #e6e6e6;
    --paper-dark: #d3d3d3;
    --navy: #0f2c55;
    --subtitle-gray: #6e6e6e;
    --body-text: #5a5a5a;
    --footer-text: #3f3f3f;
    --rule-dark: #3a3a3a;
  }
  * { margin: 0; padding: 0; box-sizing: border-box; }
  html, body {
    width: 1023px; height: 1200px; overflow: hidden;
    background: var(--backdrop);
  }
  .letterhead {
    position: absolute; left: 83px; top: 0;
    width: 845px; height: 1185px;
    transform: scale(1.0127); transform-origin: top left;
    background: linear-gradient(90deg, var(--paper-light) 0%, var(--paper-dark) 60%, var(--paper-dark) 100%);
    font-family: "Didact Gothic", "Century Gothic", sans-serif;
  }
  .brand {
    position: absolute; top: 86px; left: 0; right: 0; text-align: center;
    font-family: "Roboto", sans-serif;
  }
  .brand-name {
    display: block; font-weight: 700; font-size: 50px; line-height: 1;
    color: var(--navy); letter-spacing: 1px; margin-left: 8px;
  }
  .brand-descriptor {
    display: block; margin-top: 4px; margin-left: 12px;
    font-weight: 400; font-size: 14.5px; letter-spacing: 3.1px;
    color: var(--subtitle-gray);
  }
  .letter-body {
    position: absolute; left: 80px; top: 310px; width: 695px;
    color: var(--body-text);
  }
  .salutation { font-size: 16px; color: #4a4a4a; margin-bottom: 38px; }
  .letter-body p.para {
    font-size: 12.6px; line-height: 18px; text-align: justify; margin-bottom: 18px;
  }
  .letter-body p.para.spaced { margin-top: 36px; }
  .closing { font-size: 12.6px; margin-top: 72px; }
  .footer {
    position: absolute; left: 63px; top: 1085px; width: 713px; height: 32px;
    border-top: 1px solid var(--rule-dark);
    border-bottom: 1.5px solid var(--navy);
    display: flex; align-items: center; justify-content: space-between;
    padding: 0 15px 0 14px;
    font-family: "Roboto", sans-serif; font-size: 12.5px; color: var(--footer-text);
  }
  .contact-list { display: flex; gap: 6px; align-items: center; margin-top: -3px; }
  .contact-item { display: flex; align-items: center; gap: 6px; }
  .contact-item svg { width: 11px; height: 11px; fill: var(--navy); }
  .address { margin-top: 2px; }
</style>
</head>
<body>
  <main class="letterhead">
    <header class="brand">
      <span class="brand-name">VITORRANE</span>
      <span class="brand-descriptor">COMMUNITY HEALTH CENTER</span>
    </header>

    <section class="letter-body">
      <p class="salutation">Dear Martin,</p>
      <p class="para">Donec malesuada orci vitae nulla accumsan porta a id massa. Quisque accumsan iaculis magna sit amet fringilla. Maecenas consequat, magna eget tincidunt semper, odio nibh rutrum mi, id feugiat ante nisi eu risus. Vestibulum nunc orci, rhoncus a placerat in, ultricies in mi. Cras mattis varius eros, vel fringilla nisi suscipit eget. Quisque scelerisque sagittis nulla at porttitor.</p>
      <p class="para">Lorem ipsum dolor sit amet, consectetur adipiscing elit. Donec orci purus, luctus vitae dignissim eu, iaculis sed purus. Vivamus faucibus, ipsum nec aliquet viverra, leo mauris condimentum ligula, sit amet sagittis enim ligula quis arcu. Nam egestas tortor id nisi porttitor mattis. In tortor ante, ultricies in suscipit a, tempus non massa. Vivamus et auctor mi. Fusce vel massa nulla. Phasellus nec eros mauris, et scelerisque orci.</p>
      <p class="para spaced">It is a long established fact that a reader will be distracted by the readable content of a page when looking at its layout. The point of using Lorem Ipsum is that it has a more-or-less normal distribution of letters, as opposed to using 'Content here, content here', making it look like readable English. Many desktop publishing packagest</p>
      <p class="para">Sed id augue vitae urna euismod commodo aliquet a quam. Pellentesque arcu velit, cursus et malesuada ut, consequat et diam. Nullam erat sem, rhoncus id ullamcorper vitae, rhoncus et arcu. In ultricies ultricies nulla, ut rutrum nisi iaculis at. Donec eu magna a metus ornare faucibus. Fusce aliquet faucibus ultricies. Morbi semper, est id tincidunt gravida, sem arcu adipiscing lacus, ac bibendum nulla leo eu purus. Quisque nec diam sed risus consectetur a ccumsan quis quis nibh. Vestibulum id purus lorem.</p>
      <p class="closing">Sincerely,</p>
    </section>

    <footer class="footer">
      <span class="address">PO Box 512 Larkfield, Oregon 97321</span>
      <div class="contact-list">
        <span class="contact-item">
          <svg viewBox="0 0 24 24" aria-hidden="true"><path d="M6.6 10.8a15.2 15.2 0 0 0 6.6 6.6l2.2-2.2c.3-.3.7-.4 1-.2 1.1.4 2.3.6 3.6.6.6 0 1 .4 1 1V20c0 .6-.4 1-1 1A17 17 0 0 1 3 4c0-.6.4-1 1-1h3.5c.6 0 1 .4 1 1 0 1.3.2 2.5.6 3.6.1.3 0 .7-.2 1z"/></svg>
          (541) 330.4812
        </span>
        <span class="contact-item">
          <svg viewBox="0 0 24 24" aria-hidden="true"><path d="M2 5h20v14H2z M2 5l10 8 10-8" /></svg>
          info@vitorrane-health.org
        </span>
        <span class="contact-item">
          <svg viewBox="0 0 24 24" aria-hidden="true"><circle cx="12" cy="12" r="10"/><path d="M7 7c2 0 3 1 3 3s-2 2-2 4 2 2 2 4M15 4c0 2 2 3 2 5s-2 2-3 3 1 3 3 4" fill="none" stroke="#fff" stroke-width="1.6"/></svg>
          www.vitorrane-health.org
        </span>
      </div>
    </footer>
  </main>
</body>
</html>
```